南谷 睦月というペンネームで活動しているものです。

本業は組織・人財開発領域に特化した支援を行う会社において、
企画の提案、プロジェクトマネジメント、依頼後の進捗管理など、
お客様の中に自身も入りながら、経営を変えていくような支援を行っています。

ご依頼をさせていただく表紙デザインですが、
9月16日にPagoraにて、下記の内容を発行いたしました。
============================
現場を変える人が大切にする4つの視点:
~挑戦した人々の物語から静かに学び取る~

www.bookvale-store.jp/item/Q72KD4MX3N
こちらの内容について、発行に向けた表紙手配が間に合わなかったこともあり、
一旦はデザインを自身で考え、発行をいたしましたが、
表紙は書籍の顔ということもあり、作成依頼を進めることに決めました。

デザイン制作にあたって検討いただきたいのは下記2点です。

検討に当たってのポイントは下記2点です。
① 悩みに対しての答えが見つかるような印象を持てる
② あまり複雑すぎないデザインであること

① 悩みに対しての答えが見つかるような印象を持てる
・取り上げたPagoraでは、スキル・ノウハウ本ではなく、
実践されている方が直面されたエピソードをもとにして、
悩みを解決するためのヒントを取り上げています。
そのようなニュアンスが感じられるようなデザインに期待です。

② あまり複雑なデザインではないこと
・凝ったデザインよりは、わかりやすいデザインを好む方です。
複雑なカラーよりは、色を限りながらも、与えられた題材に対しての
表現を頂けるようなデザインが好みではあります。
※ が、良いものが出てくれば、それ限りではございませんので、
あくまで、現時点の好みとしてお伝えを致します

最終的に今回のコンペでは「R_hoshidaさん」のデザインを採用させて頂きます。
重視した点は改めて、下記の2点がベースとなります。
① 悩みに対しての答えが見つかるような印象を持てる
② あまり複雑なデザインではないこと
絵で①のイメージを喚起しつつ、今回の書籍で押し出していることを文字で強調いただく構成となっており、②の点からも適切と考えて採択をさせて頂きました。

改めて、この度はご提案をいただきましてありがとうございます。

引き続き、個人的な目標としては3か月~6か月に1回の頻度で、
Pagora向けの発行物を執筆していく予定です。
また、このような形でご支援の相談をさせていただきますので、
よろしければ是非、お力添えをどうぞお願い申し上げます。

```html
<!DOCTYPE html>
<html lang="ja">
<head>
<meta charset="utf-8">
<title>現場を変える人が大切にする4つの視点 — 南谷 睦月</title>
<link rel="stylesheet" href="https://fonts.googleapis.com/css2?family=Noto+Sans+JP:wght@500;700;900&display=swap">
<style>
  :root {
    --ink: #1f1f1f;
    --paper: #ffffff;
    --accent: #f6c21c;
    --accent-deep: #eea500;
    --navy: #2c3443;
    --figure-tone: #e9dfc6;
  }
  * { margin: 0; padding: 0; box-sizing: border-box; }
  html, body { width: 749px; height: 1200px; overflow: hidden; background: var(--paper); }
  .cover {
    position: relative; width: 749px; height: 1200px; overflow: hidden;
    background: var(--paper); color: var(--ink);
    font-family: "Noto Sans JP", sans-serif; font-weight: 900;
  }
  .title-line { position: absolute; white-space: nowrap; line-height: 1; display: block; }
  .title-line--1 { left: 60px; top: 30px; font-size: 100px; }
  .title-line--1 .main { position: relative; z-index: 1; }
  .title-line--1 .main::after {
    content: ""; position: absolute; left: -4px; right: -4px; bottom: -8px; height: 18px;
    background: var(--accent); z-index: -1; border-radius: 4px;
  }
  .title-sub { position: absolute; right: 60px; top: 158px; font-size: 42px; line-height: 1; white-space: nowrap; }
  .title-line--2 { left: 0; width: 749px; text-align: center; top: 212px; font-size: 88px; }
  .title-line--3 { left: 0; width: 749px; text-align: center; top: 335px; }
  .title-line--3 .num { font-size: 165px; color: var(--accent-deep); }
  .title-line--3 .particle { font-size: 62px; margin: 0 4px; }
  .title-line--3 .key { font-size: 145px; position: relative; z-index: 1; }
  .title-line--3 .key::after {
    content: ""; position: absolute; left: 0; right: 0; bottom: 4px; height: 22px;
    background: var(--accent); z-index: -1; border-radius: 4px;
  }
  .author { position: absolute; left: 0; width: 749px; text-align: center; top: 540px; }
  .author-name { font-size: 40px; font-weight: 700; letter-spacing: 6px; line-height: 1.2; }
  .author-roman { font-size: 16px; font-weight: 500; letter-spacing: 2px; margin-top: 4px; }

  .journey { position: absolute; left: 0; top: 610px; width: 749px; height: 260px; }

  .message {
    position: absolute; left: 0; top: 875px; width: 749px; height: 325px;
    background: var(--accent); text-align: center;
  }
  .message-line { position: absolute; left: 0; width: 749px; white-space: nowrap; line-height: 1; }
  .message-line--1 { top: 22px; font-size: 54px; }
  .message-line--2 { top: 96px; font-size: 54px; }
  .message-line--3 { top: 214px; font-size: 60px; }
  .message .big { font-size: 76px; }
  .message-line--3 .big { font-size: 86px; }
  .message .mark { background: var(--paper); padding: 2px 4px; border-radius: 4px; }
</style>
</head>
<body>
<main class="cover">
  <h1 class="title">
    <span class="title-line title-line--1"><span class="main">現場を変える</span></span>
    <span class="title-sub">人が</span>
    <span class="title-line title-line--2">大切にする</span>
    <span class="title-line title-line--3"><span class="num">4</span><span class="particle">つの</span><span class="key">視点</span></span>
  </h1>

  <div class="author">
    <p class="author-name">南谷 睦月</p>
    <p class="author-roman">Minamitani Mutsuki</p>
  </div>

  <svg class="journey" viewBox="0 0 749 260" aria-label="悩みから行動を経て解決へ">
    <g fill="none" stroke="#1f1f1f" stroke-width="5">
      <line x1="560" y1="190" x2="425" y2="190"/>
      <line x1="325" y1="190" x2="190" y2="190"/>
    </g>
    <g fill="#1f1f1f">
      <polygon points="415,190 435,178 435,202"/>
      <polygon points="180,190 200,178 200,202"/>
    </g>
    <circle cx="100" cy="150" r="75" fill="var(--navy)"/>
    <rect x="68" y="88" width="64" height="92" rx="24" fill="var(--figure-tone)" role="img" aria-label="問題を解決して喜ぶ人物のイラスト"/>
    <circle cx="650" cy="150" r="75" fill="var(--navy)"/>
    <rect x="618" y="88" width="64" height="92" rx="24" fill="var(--figure-tone)" role="img" aria-label="腕を組んで悩む人物のイラスト"/>
    <rect x="325" y="30" width="100" height="150" rx="36" fill="var(--figure-tone)" role="img" aria-label="鞄を持って歩き出す人物のイラスト"/>
    <circle cx="375" cy="190" r="40" fill="var(--paper)" stroke="#1f1f1f" stroke-width="4"/>
    <g font-family="Noto Sans JP, sans-serif" font-weight="700" font-size="24" text-anchor="middle">
      <text x="100" y="208" fill="#ffffff">解決</text>
      <text x="375" y="199" fill="#1f1f1f">行動</text>
      <text x="650" y="208" fill="#ffffff">悩み</text>
    </g>
  </svg>

  <section class="message">
    <p class="message-line message-line--1">実践されている人たちの</p>
    <p class="message-line message-line--2"><span class="big mark">経験</span>を<span class="big mark">紐解き</span>ながら</p>
    <p class="message-line message-line--3"><span class="big">解決</span>する<span class="big">ヒント</span>満載</p>
  </section>
</main>
</body>
</html>
```